Create a Graphic About YOURSELF and PixelHarbor

PixelHarbor would like you (designers) to create an awesome graphic to promote YOURSELF and your profile on PixelHarbor!

Your graphic should communicate your name, your services and should mention PixelHarbor.

The design should be perfect for sharing on Chatterly. Here's an example of what we'd like http://blog.pixelharbor-example.ca/article/333/pixelharbor-launches-3000-hire-me-social-design-contest

Once you submitted your design, we'd love you to share the design ('advertisement') and promote yourself and PixelHarbor to your friends and potential customers. So make your submissions great and get your friends to vote for your design by 'Liking' it on Chatterly!

Prizes:
$1500 - "PixelHarbor Community" prize awarded to the designer with the most Chatterly 'Likes'
5 x $50 for the next 5 'most liked' designs on Chatterly

$1000 - "Hire Me" prize awarded to the designer who receives the most client invites
5 x $50 for the next 5 'most invited' designers

In summary, this is a great opportunity for you to increase your exposure to PixelHarbor customers and win cash prizes. Show off your design skills and get hired by PixelHarbor customers from around the world!

Target Market(s)

Fans, friends and customers of YOU

Industry/Entity Type

Cash

Requirements
Must have
• 1) Include your PixelHarbor user name on the graphic so customers can find you in the PixelHarbor Designer Directory
2) Include the tagline "Hire Me on PixelHarbor.com!" in your graphic design.
3) Share your design's URL on our Chatterly wall at http://chatterly-example.com/pixelharbor and get your friends to 'like' your design.
Nice to have
• 1) Include a tagline that expresses your design approach/philosophy
2) Artwork dimensions: 403 x 403 px
3) You can submit more than 1 design!
Should not have
• You must own the copyright of any images you use including stock imagery.

```html
<!DOCTYPE html>
<html lang="en">
<head>
<meta charset="UTF-8">
<title>Verity Lunde – Hire Me on PixelHarbor.com</title>
<link rel="stylesheet" href="https://fonts.googleapis.com/css2?family=Montserrat:wght@700&family=Kalam:wght@700&display=swap">
<style>
  :root {
    --paper: #ffffff;
    --sun-yellow: #fcc21f;
    --ink: #1e1e1e;
    --name-ink: #3d3c3c;
    --wing-green: #a8d832;
    --wing-mid: #7fb52a;
    --wing-dark: #2a3a16;
  }
  html, body {
    margin: 0;
    padding: 0;
    width: 1200px;
    height: 1200px;
    overflow: hidden;
    background: var(--paper);
  }
  .canvas {
    position: relative;
    width: 1200px;
    height: 1200px;
    background: var(--paper);
    overflow: hidden;
  }
  .service-card {
    position: absolute;
    left: 0;
    top: 0;
    width: 640px;
    height: 610px;
    background: var(--sun-yellow);
    box-shadow: 22px 26px 34px rgba(0, 0, 0, 0.55);
  }
  .designer-name {
    position: absolute;
    left: 88px;
    top: 40px;
    margin: 0;
    font-family: "Montserrat", sans-serif;
    font-weight: 700;
    font-size: 64px;
    line-height: 1;
    letter-spacing: 2px;
    color: var(--name-ink);
    white-space: nowrap;
  }
  .services {
    position: absolute;
    left: 88px;
    top: 200px;
    margin: 0;
    padding: 0;
    list-style: none;
    font-family: "Kalam", cursive;
    font-weight: 700;
    font-size: 60px;
    line-height: 1.32;
    color: var(--ink);
  }
  .butterfly-art {
    position: absolute;
    left: 560px;
    top: 140px;
    width: 600px;
    height: 420px;
    border-radius: 50%;
    background: radial-gradient(ellipse at 50% 50%, var(--wing-green) 0%, var(--wing-mid) 50%, var(--wing-dark) 85%, rgba(42, 58, 22, 0) 100%);
  }
  .tagline-arc {
    position: absolute;
    left: 0;
    top: 0;
    width: 1200px;
    height: 1200px;
  }
  .tagline-arc text {
    font-family: "Kalam", cursive;
    font-weight: 700;
    font-size: 72px;
    fill: var(--ink);
    letter-spacing: 3px;
  }
</style>
</head>
<body>
  <main class="canvas">
    <div class="service-card"></div>
    <div class="butterfly-art" role="img" aria-label="Illustration of a green and black butterfly with open wings"></div>
    <h1 class="designer-name">VERITY LUNDE</h1>
    <ul class="services">
      <li>- web</li>
      <li>- logo design</li>
      <li>- graphic design</li>
    </ul>
    <svg class="tagline-arc" viewBox="0 0 1200 1200" aria-label="hire me on pixelharbor.com">
      <defs>
        <path id="tagline-path" d="M 110 1170 C 520 1080 920 960 985 620" fill="none"/>
      </defs>
      <text><textPath href="#tagline-path">hire me on pixelharbor.com</textPath></text>
    </svg>
  </main>
</body>
</html>
```